Create Brisk Lesson Studio a card design that will stick in the mind of prospects.

Brisk Lesson Studio specialises designs and produces training video, animation, illustration and text.

We need a card design that oozes class and leaves the prospect brimming with confidence.

The design will feature the Brisk Lesson Studio all black logo (uploaded). The design may also use the shade of orange from the orange version of the logo (uploaded). Note, just the color is to be used e.g. for the back of the card, not the orange logo itself.

The Brisk brand is about authenticity, quality, maturity and assurance. We are a safe buy when it comes to the prospects next project.

Target Market(s)

The primary target is training managers or others who are responsible for choosing to hire companies to produce their training media e.g. video. This will usually be a large spend so they need to have confidence.

Industry/Entity Type

Training

Contact Information for Business Card

FRONT:

Brisk Lesson Studio
Phone: 03 5172 4039
1st Floor, 418 Kellerby Road
Mt Ferncombe
VIC 3862
Australia
www.brisklesson.com.au

Lionel Petch
Founder and Lead Consultant
mobile: +61 3 0462 735 218
email: lionel@brisklesson.com.au

BACK:
Specialising in design and production of training:

video
animation
illustration
text

for delivery via internet, intranet and/or LMS.

Number of Pages Required

4 page

Font styles to use
Sans Serif

Requirements
Must have
• The black logo uploaded with the brief.
Nice to have
• The inclusion of the shade of orange found in the orange logo also uploaded with the brief. One example would be having the back of the card in this orange and using a white font for the text. But I want the designer to work this out.
Should not have
• No colours other than black and the orange included in the uploaded orange logo.

```html
<!DOCTYPE html>
<html lang="en">
<head>
<meta charset="utf-8">
<title>Brisk Lesson Studio — Business Card</title>
<link rel="stylesheet" href="https://fonts.googleapis.com/css2?family=Open+Sans:wght@400;600;700&display=swap">
<style>
  :root {
    --backdrop: #3b3431;
    --card: #0c0c0c;
    --card-back: #1a1a1a;
    --ink: #f2f2f2;
    --ink-soft: #d6d6d6;
    --rule: #4a4a4a;
  }
  * { box-sizing: border-box; margin: 0; padding: 0; }
  html, body { width: 1200px; height: 900px; overflow: hidden; }
  body {
    background: var(--backdrop);
    font-family: "Open Sans", Arial, sans-serif;
    color: var(--ink);
    position: relative;
  }
  .card {
    position: absolute;
    top: 290px;
    width: 520px;
    height: 310px;
    border-radius: 4px;
    box-shadow: 0 10px 30px rgba(0,0,0,0.45);
  }
  .card-front { left: 60px; background: var(--card); }
  .card-back { left: 620px; background: var(--card-back); }

  .person {
    position: absolute;
    top: 44px; left: 30px;
    width: 210px;
    text-align: right;
    font-size: 13px;
    line-height: 1.55;
    color: var(--ink-soft);
  }
  .person-name { font-weight: 700; font-size: 16px; color: var(--ink); }
  .person-role { margin-bottom: 10px; }
  .contact-line { display: flex; justify-content: flex-end; align-items: center; gap: 8px; }
  .contact-line svg { width: 11px; height: 11px; flex: none; }

  .divider {
    position: absolute;
    top: 40px; left: 262px;
    width: 1px; height: 104px;
    background: var(--rule);
  }
  .company {
    position: absolute;
    top: 40px; left: 282px;
    font-size: 12.5px;
    line-height: 1.5;
    color: var(--ink-soft);
  }
  .company-address { margin-bottom: 14px; }
  .company .contact-line { justify-content: flex-start; }

  .wordmark-front {
    position: absolute;
    left: 0; right: 0;
    bottom: 46px;
    text-align: center;
    font-weight: 700;
    font-size: 78px;
    letter-spacing: 1px;
    color: var(--ink);
  }

  .brand-lockup {
    position: absolute;
    top: 46px; left: 0; right: 0;
    display: flex; justify-content: center; align-items: center; gap: 14px;
  }
  .brand-lockup .mark {
    width: 40px; height: 40px; border-radius: 50%;
    border: 2px solid var(--ink);
  }
  .brand-name { font-weight: 700; font-size: 28px; color: var(--ink); }

  .services {
    position: absolute;
    top: 150px; left: 0; right: 0;
    text-align: center;
    font-size: 14.5px;
    font-weight: 600;
    line-height: 1.9;
    color: var(--ink);
  }
</style>
</head>
<body>
  <section class="card card-front" aria-label="Business card front">
    <div class="person">
      <p class="person-name">Lionel Petch</p>
      <p class="person-role">Founder and Lead Consultant</p>
      <p class="contact-line">+61 3 0462 735 218
        <svg viewBox="0 0 12 12" aria-hidden="true"><rect x="3" y="0.5" width="6" height="11" rx="1" fill="none" stroke="currentColor"/><circle cx="6" cy="9.5" r="0.7" fill="currentColor"/></svg>
      </p>
      <p class="contact-line">lionel@brisklesson.com.au
        <svg viewBox="0 0 12 12" aria-hidden="true"><rect x="0.5" y="2.5" width="11" height="7" fill="currentColor"/><path d="M0.5 2.5 L6 7 L11.5 2.5" fill="none" stroke="#0c0c0c"/></svg>
      </p>
    </div>
    <div class="divider"></div>
    <div class="company">
      <p class="company-address">1st Floor, 418 Kellerby Road<br>Mt Ferncombe VIC 3862 Australia</p>
      <p class="contact-line">
        <svg viewBox="0 0 12 12" aria-hidden="true"><path d="M2 1 L4.5 1 L5.5 4 L4 5 Q5 7.5 7 8 L8 6.5 L11 7.5 L11 10 Q6 11 2 6 Q1 3.5 2 1Z" fill="currentColor"/></svg>
        03 5172 4039</p>
      <p class="contact-line">
        <svg viewBox="0 0 12 12" aria-hidden="true"><circle cx="6" cy="6" r="5.5" fill="currentColor"/><path d="M0.5 6 H11.5 M6 0.5 Q3 6 6 11.5 M6 0.5 Q9 6 6 11.5" fill="none" stroke="#0c0c0c" stroke-width="0.8"/></svg>
        www.brisklesson.com.au</p>
    </div>
    <p class="wordmark-front">Brisk</p>
  </section>

  <section class="card card-back" aria-label="Business card back">
    <div class="brand-lockup">
      <span class="mark" aria-hidden="true"></span>
      <span class="brand-name">Brisk Lesson Studio</span>
    </div>
    <div class="services">
      <p>Specialising in design and production of training</p>
      <p>Video | Animation | Illustration | Text</p>
      <p>for delivery via internet, intranet and/or LMS.</p>
    </div>
  </section>
</body>
</html>
```